LED Horticulture / Garden Grow Light Company Seeks Product & Company Brochure / Catalog

Verdant Beam Works, LLC builds high intensity LED gardening / grow lights for horticulture. Greenhouse lighting, indoor gardening lighting and the hydroponics industry. The company is seeking a company brochure and/or catalog that features the product, The VBW 550 and a background on the company.

The company is also interested in using these layouts in templates for product packaging design such as standups in stores and box printing.

Target Market(s)

Indoor gardening industry and hobbyists, hydroponics supply stores, pelham's sunny sprout, medical marijuana / cannabis cultivators and legal states such as Colorado.

Industry/Entity Type

It Company

Colors

Designer to choose colors to be used in the design.

Requirements
Must have
• Showcase the products / company and have a layout that can be incorporated amongst other printed marketing materials including packaging and catalogs. Competitors are the following: http://lumivarro.com https://www.ostrelpanel.com/ http://www.torvanix.com/retail https://quillara.science/ https://www.brightmeadowpanel.com/

```html
<!DOCTYPE html>
<html lang="en">
<head>
<meta charset="utf-8">
<title>Verdant Beam Works — High Intensity LED Grow Lights 2013</title>
<link rel="stylesheet" href="https://fonts.googleapis.com/css2?family=Montserrat:ital,wght@0,500;0,600;1,700&display=swap">
<style>
  :root {
    --stage: #e9eaea;
    --paper: #ffffff;
    --green-deep: #5a9e3e;
    --green-light: #8cc63f;
    --panel-light: #f1f2f2;
    --panel-mid: #c9cbcc;
    --grow-magenta: #b43cc8;
    --grow-violet: #d65fe0;
    --leaf-green: #4f8f2c;
    --ink-white: #ffffff;
    --ink-green: #4f8f35;
  }
  html, body {
    margin: 0;
    padding: 0;
    width: 1179px;
    height: 1200px;
    overflow: hidden;
    background: var(--stage);
  }
  .canvas {
    position: relative;
    width: 1179px;
    height: 1200px;
  }
  .cover {
    position: absolute;
    left: 269px;
    top: 160px;
    width: 640px;
    height: 880px;
    background: var(--paper);
    box-shadow: 0 14px 40px rgba(0,0,0,0.18);
  }
  .cover svg { display: block; }
  .title {
    font-family: "Montserrat", sans-serif;
    font-style: italic;
    font-weight: 700;
    font-size: 44px;
    fill: var(--ink-white);
  }
  .edition {
    font-family: "Montserrat", sans-serif;
    font-weight: 500;
    font-size: 44px;
    fill: var(--ink-white);
  }
  .brand-name {
    font-family: "Montserrat", sans-serif;
    font-weight: 600;
    font-size: 30px;
    fill: var(--ink-green);
  }
</style>
</head>
<body>
<main class="canvas">
  <section class="cover" aria-label="Brochure cover">
    <svg width="640" height="880" viewBox="0 0 640 880" xmlns="http://www.w3.org/2000/svg">
      <defs>
        <linearGradient id="panelTone" x1="0" y1="0" x2="1" y2="1">
          <stop offset="0" stop-color="var(--panel-mid)"/>
          <stop offset="0.5" stop-color="var(--panel-light)"/>
          <stop offset="1" stop-color="var(--panel-mid)"/>
        </linearGradient>
        <linearGradient id="growTone" x1="0" y1="0" x2="1" y2="1">
          <stop offset="0" stop-color="var(--grow-violet)"/>
          <stop offset="0.55" stop-color="var(--grow-magenta)"/>
          <stop offset="1" stop-color="var(--leaf-green)"/>
        </linearGradient>
      </defs>

      <!-- header band -->
      <polygon class="header-band" points="0,0 640,0 640,160 0,330" fill="var(--green-deep)"/>
      <polygon class="edition-wedge" points="640,40 640,215 360,290 0,330 0,330" fill="var(--green-light)"/>
      <polygon class="header-band-top" points="0,0 640,0 640,40 0,330" fill="var(--green-deep)"/>

      <text class="title" transform="translate(48 228) rotate(-13)">
        <tspan x="0" y="0">High Intensity LED</tspan>
        <tspan x="0" y="52">Grow Lights</tspan>
      </text>
      <text class="edition" transform="translate(492 214) rotate(-13)">2013</text>

      <!-- photo strip -->
      <polygon class="photo-panels" role="img" aria-label="Photo of LED grow light panels hanging above plants"
               points="0,338 300,298 250,560 0,600" fill="url(#panelTone)"/>
      <polygon class="photo-greens" role="img" aria-label="Photo of fresh lettuce held under magenta grow light"
               points="312,296 640,222 640,470 262,560" fill="url(#growTone)"/>
      <line x1="306" y1="297" x2="256" y2="560" stroke="var(--paper)" stroke-width="10"/>

      <!-- brand -->
      <rect class="brand-mark" x="64" y="668" width="44" height="44" rx="6" fill="var(--green-light)"/>
      <text class="brand-name" x="124" y="701">Verdant Beam Works</text>

      <!-- footer band -->
      <polygon class="footer-band" points="0,810 640,790 640,880 0,880" fill="var(--green-deep)"/>
      <polygon class="footer-accent" points="0,810 180,804 120,880 0,880" fill="var(--green-light)"/>
    </svg>
  </section>
</main>
</body>
</html>
```